Web Design Project

Create a web design

Target Market(s)

Upper class people interested in health

Requirements
Must have
• Templates
Nice to have
• Use the logo provided

```html
<!DOCTYPE html>
<html lang="en">
<head>
<meta charset="utf-8">
<title>Verdance health &amp; fitness</title>
<link rel="stylesheet" href="https://fonts.googleapis.com/css2?family=Oswald:wght@400;500&family=Arimo:wght@400&display=swap">
<style>
:root{
  --green:#4ee23a;
  --footer-green:#22f04e;
  --blue:#1a96e4;
  --accent-blue:#1565c8;
  --ink:#0b1420;
  --white:#ffffff;
  --grey:#6d6d6d;
}
*{margin:0;padding:0;box-sizing:border-box}
html,body{width:1200px;height:1200px;overflow:hidden;background:var(--white)}
body{position:relative;font-family:"Oswald",sans-serif;color:var(--ink)}
.hero{position:absolute;left:0;top:0;width:1200px;height:557px;overflow:hidden;
  background:radial-gradient(ellipse 520px 420px at 545px 230px,#4fe03a 0%,#8ff07e 35%,#d6f9cf 65%,#ffffff 100%)}
.brand-plate{position:absolute;left:0;top:25px;width:375px;height:100px}
.brand{position:absolute;left:38px;top:38px;display:flex;align-items:center;gap:10px;
  font-weight:400;font-size:40px;letter-spacing:1px;color:var(--grey);line-height:1}
.brand-dot{width:30px;height:30px;border-radius:50%;background:var(--accent-blue)}
.brand-tag{position:absolute;left:70px;top:91px;font-size:17px;letter-spacing:3px;color:var(--grey)}
.nav{position:absolute;left:358px;top:53px;display:flex;gap:16px;list-style:none}
.nav a{font-size:19.5px;letter-spacing:-0.2px;text-transform:uppercase;color:var(--ink);text-decoration:none;line-height:28px}
.nav a.current{color:var(--accent-blue);text-decoration:underline;text-underline-offset:3px}
.hero-photo{position:absolute;left:690px;top:100px;width:405px;height:457px;
  background:linear-gradient(180deg,#e8f3ff 0%,#cfe2f5 50%,#c4cfdb 100%)}
.headline{position:absolute;left:152px;top:216px;font-size:30px;font-weight:400;line-height:37px;text-transform:uppercase}
.headline em{font-style:normal;color:var(--accent-blue)}
.lede{position:absolute;left:152px;top:335px;font-size:19px;line-height:29px;letter-spacing:0.3px;text-transform:uppercase}
.social{position:absolute;left:148px;top:468px;display:flex;gap:10px}
.social span{width:72px;height:72px;border-radius:12px;box-shadow:0 3px 5px rgba(0,0,0,.3)}
.social .s1{background:#3b5b9c}.social .s2{background:#4cc0e6}.social .s3{background:#e8e8e8}
.dots{position:absolute;left:791px;top:521px;display:flex;gap:10px}
.dots span{width:12px;height:12px;background:var(--white)}
.dots .on{background:var(--green)}
.services{position:absolute;left:0;top:557px;width:1200px;height:338px;background:var(--blue)}
.service{position:absolute;top:16px}
.service h2,.news-title{font-size:23px;font-weight:400;text-transform:uppercase;color:var(--ink);line-height:30px}
.service p{font-size:15px;line-height:22px;color:var(--white);text-transform:uppercase}
.service a{display:block;margin-top:3px;font-size:15px;color:var(--ink);text-decoration:none;text-transform:uppercase}
.divider{position:absolute;left:190px;top:143px;width:860px;height:30px;
  background:radial-gradient(ellipse 50% 40% at 50% 20%,rgba(0,40,90,.28),transparent)}
.news-title{position:absolute;left:182px;top:182px}
.news{position:absolute;top:226px;display:flex;gap:11px;width:285px}
.news-thumb{width:88px;height:88px;flex:none}
.news h3{font-size:23px;font-weight:400;color:var(--white);line-height:20px;margin-top:-2px;text-transform:uppercase}
.news p{font-family:"Arimo",sans-serif;font-size:12px;line-height:14.5px;color:#000;margin-top:10px}
.arrow{position:absolute;top:230px;font-family:"Arimo",sans-serif;font-size:56px;color:var(--white);font-weight:700}
.partners{position:absolute;left:0;top:895px;width:1200px;height:163px}
.footer{position:absolute;left:0;top:1058px;width:1200px;height:142px;background:var(--footer-green);
  font-family:"Arimo",sans-serif;font-size:14px;color:#000;text-align:center}
.footer ul{list-style:none;display:flex;justify-content:center;gap:24px;margin-top:31px}
.footer a{color:#000;text-decoration:none}
.footer p{margin-top:1px}
</style>
</head>
<body>
<header class="hero">
  <svg class="brand-plate" viewBox="0 0 375 100" aria-hidden="true"><polygon points="0,0 375,0 270,100 0,100" fill="#fff"/></svg>
  <div class="brand">VERDANCE<span class="brand-dot"></span></div>
  <div class="brand-tag">health &amp; fitness</div>
  <div class="hero-photo" role="img" aria-label="Photo of a smiling woman in blue sportswear holding an exercise ball"></div>
  <ul class="nav">
    <li><a class="current" href="#">Home</a></li>
    <li><a href="#">About us</a></li>
    <li><a href="#">Services</a></li>
    <li><a href="#">Packages</a></li>
    <li><a href="#">Clients</a></li>
    <li><a href="#">Contact us</a></li>
  </ul>
  <h1 class="headline">Donec <em>in velit tellus</em><br>Duis at est ipsum, <em>id consectetur</em> ante<br><em>Quisque</em> ut velit <em>justo,</em> id suscipit est</h1>
  <p class="lede">Etiam eu bibendum odio. Curabitur quis lacus nunc.<br>Morbi commodo est sed neque tempor in aliquet nisi suscipit.<br>Suspendisse ut varius augue.</p>
  <div class="social" aria-label="Social links"><span class="s1"></span><span class="s2"></span><span class="s3"></span></div>
  <div class="dots"><span></span><span class="on"></span><span></span><span></span></div>
</header>

<section class="services">
  <div class="service" style="left:182px">
    <h2>Fitness assessment</h2>
    <p>Fitness testing before a<br>nd after 10th and 20th<br>training session to establish ...</p>
    <a href="#">&gt; More</a>
  </div>
  <div class="service" style="left:482px">
    <h2>Nutritional planning</h2>
    <p>If you need for more<br>structure we can also formulate<br>a 7 to 14 day diet plan ...</p>
    <a href="#">&gt; More</a>
  </div>
  <div class="service" style="left:797px">
    <h2>Muscle &amp; strength gain</h2>
    <p>Come to us and find new<br>ways of driving muscle<br>and strength gain...</p>
    <a href="#">&gt; More</a>
  </div>
  <div class="divider"></div>
  <h2 class="news-title">News</h2>
  <span class="arrow" style="left:120px">&lt;</span>
  <article class="news" style="left:182px">
    <div class="news-thumb" role="img" aria-label="Sports news photo" style="background:linear-gradient(135deg,#ffffff,#e9e9e9)"></div>
    <div><h3>Lorem ipsum</h3><p>dolor sit amet, consectetur adipiscing elit. Aliquam sodales, nulla ac consectetur vulputate,...</p></div>
  </article>
  <article class="news" style="left:471px">
    <div class="news-thumb" role="img" aria-label="Bodybuilder in gym photo" style="background:linear-gradient(135deg,#3a2a22,#6a4a36)"></div>
    <div><h3>Lorem ipsum</h3><p>dolor sit amet, consectetur adipiscing elit. Aliquam sodales, nulla ac consectetur vulputate,...</p></div>
  </article>
  <article class="news" style="left:757px">
    <div class="news-thumb" role="img" aria-label="Black and white training photo" style="background:linear-gradient(135deg,#e0e0e0,#7a7a7a)"></div>
    <div><h3>Lorem ipsum</h3><p>dolor sit amet, consectetur adipiscing elit. Aliquam sodales, nulla ac consectetur vulputate,...</p></div>
  </article>
  <span class="arrow" style="left:1047px">&gt;</span>
</section>

<section class="partners" aria-label="Partners">
  <svg width="1200" height="163" viewBox="0 0 1200 163" aria-hidden="true">
    <rect x="205" y="55" width="65" height="70" rx="4" fill="#d8d8d8"/>
    <rect x="364" y="66" width="86" height="51" fill="none" stroke="#8a8a8a" stroke-width="2"/>
    <rect x="559" y="70" width="102" height="54" rx="12" fill="#8a8a8a"/>
    <circle cx="770" cy="88" r="38" fill="none" stroke="#8a8a8a" stroke-width="3"/>
    <rect x="914" y="52" width="122" height="78" rx="6" fill="#d0d0d0"/>
  </svg>
</section>

<footer class="footer">
  <ul>
    <li><a href="#">Home</a></li>
    <li><a href="#">About US</a></li>
    <li><a href="#">Services</a></li>
    <li><a href="#">Packages</a></li>
    <li><a href="#">Clients</a></li>
    <li><a href="#">Contact US</a></li>
  </ul>
  <p>(c) 2012 - Verdance health &amp; fitness</p>
</footer>
</body>
</html>
```